Carrowell Business Card Re-design

Our current cards are outdated. This is our website www.carrowellinsights.example. We would like something that is "on-brand" and consistent with our social media sites. We are strategic consultants with a core competency in Marketing Research. Although, please know we are considering a brand logo redesign and potentially a new look. If we like your work here we will invite you to participate when we get to that project. Thank you very much. Harriet
Here are our social sites: https://twitter.com/Carrowell?lang=en
https://plus.google.com/+Carrowellinsights
https://www.linkedin.com/company/5094827/
https://www.facebook.com/CarrowellInc/
Business

```html
<!DOCTYPE html>
<html lang="en">
<head>
<meta charset="utf-8">
<title>Carrowell Business Card</title>
<link href="https://fonts.googleapis.com/css2?family=Work+Sans:wght@400;600&display=swap" rel="stylesheet">
<style>
  :root {
    --backdrop: #cfd5d4;
    --card-white: #f3f3f0;
    --brand-green: #56b332;
    --ink: #3a3d3c;
    --card-shadow: 0 18px 40px rgba(60, 70, 70, 0.22);
  }
  * { box-sizing: border-box; margin: 0; padding: 0; }
  html, body {
    width: 1200px;
    height: 881px;
    overflow: hidden;
    background: var(--backdrop);
    font-family: "Work Sans", Arial, sans-serif;
  }
  .canvas {
    width: 1200px;
    height: 881px;
    display: flex;
    align-items: center;
    justify-content: center;
    gap: 60px;
  }
  .card {
    width: 525px;
    height: 300px;
    border-radius: 3px;
    box-shadow: var(--card-shadow);
    position: relative;
  }
  .card--front { background: var(--card-white); }
  .card--back {
    background: var(--brand-green);
    display: flex;
    align-items: center;
    justify-content: center;
  }
  .wordmark {
    font-weight: 600;
    letter-spacing: 0.5px;
    line-height: 1;
  }
  .card--front .wordmark {
    position: absolute;
    top: 40px;
    right: 38px;
    font-size: 38px;
    color: var(--brand-green);
  }
  .card--back .wordmark {
    font-size: 64px;
    color: #ffffff;
  }
  .contact {
    position: absolute;
    left: 38px;
    top: 44px;
    color: var(--ink);
    font-size: 13px;
    line-height: 1.45;
  }
  .contact__name {
    color: var(--brand-green);
    font-size: 19px;
    font-weight: 400;
    letter-spacing: 0.3px;
    line-height: 1.2;
  }
  .contact__role { margin-bottom: 4px; }
  .contact__line {
    display: flex;
    align-items: center;
    gap: 8px;
  }
  .contact__icon {
    width: 10px;
    height: 10px;
    flex: none;
    fill: var(--brand-green);
  }
</style>
</head>
<body>
<main class="canvas">
  <section class="card card--front" aria-label="Business card front">
    <div class="contact">
      <p class="contact__name">MARLOW PENNICK</p>
      <p class="contact__role">Director</p>
      <p>14-16 Ashgrove Lane</p>
      <p>Bristol, England, BS2 9QT</p>
      <p class="contact__line">
        <svg class="contact__icon" viewBox="0 0 10 10" aria-hidden="true"><path d="M2 0.5 L3.6 2.8 L2.6 3.8 C3.2 5 4.9 6.8 6.2 7.4 L7.2 6.4 L9.5 8 L8.4 9.5 C4.5 9.2 0.8 5.5 0.5 1.6 Z"/></svg>
        555.014.2287
      </p>
      <p class="contact__line">
        <svg class="contact__icon" viewBox="0 0 10 10" aria-hidden="true"><path d="M0.5 2 H9.5 V8 H0.5 Z M1 2.4 L5 5.4 L9 2.4" stroke="#f3f3f0" stroke-width="0.8"/></svg>
        info@carrowellinsights.example
      </p>
      <p class="contact__line">
        <svg class="contact__icon" viewBox="0 0 10 10" aria-hidden="true"><circle cx="5" cy="5" r="4.5"/><path d="M0.5 5 H9.5 M5 0.5 C3 3 3 7 5 9.5 M5 0.5 C7 3 7 7 5 9.5" stroke="#f3f3f0" stroke-width="0.7" fill="none"/></svg>
        www.carrowellinsights.example
      </p>
    </div>
    <p class="wordmark">carrowell</p>
  </section>

  <section class="card card--back" aria-label="Business card back">
    <p class="wordmark">carrowell</p>
  </section>
</main>
</body>
</html>
```